Weight Loss Challenge Social Media Graphics

Create 6-7 individual social media graphics (square size) to encourage folks to join our weight loss challenge. For the color scheme of the graphics, use the color palette attached

Note: each graphic can contain any of the stock photography attached or just the single picture of me (brown shirt) but a few should be ONLY the text
For some graphics we can say: JOIN US!
For some graphics, use only TEXT based

Target Market(s)

primarily women who want to get healthy

Industry/Entity Type

health and weight loss

Requirements
Must have
• The largest text should be: Ninety Days Bold

```html
<!DOCTYPE html>
<html lang="en">
<head>
<meta charset="utf-8">
<title>45 Glow Challenge – Social Graphics</title>
<link href="https://fonts.googleapis.com/css2?family=Poppins:wght@400;600;700;800&display=swap" rel="stylesheet">
<style>
  :root {
    --pink: #fcb9ca;
    --pink-light: #fde6ee;
    --pink-pale: #fff2f6;
    --mauve: #b18a84;
    --mauve-text: #a67f79;
    --cream: #f3dccb;
    --cream-pill: #f6e3d8;
    --side-word: #f3d9de;
    --ink: #3c3436;
    --white: #ffffff;
  }
  * { box-sizing: border-box; margin: 0; padding: 0; }
  html, body { width: 792px; height: 1200px; overflow: hidden; background: var(--white); }
  body { position: relative; font-family: 'Poppins', sans-serif; color: var(--ink); }

  .tile { position: absolute; width: 356px; height: 356px; overflow: hidden; }
  .col-a { left: 23px; } .col-b { left: 413px; }
  .row-1 { top: 33px; } .row-2 { top: 423px; } .row-3 { top: 812px; }

  .box { position: absolute; }
  .line { position: absolute; left: 0; right: 0; text-align: center; transform: translateY(-50%); white-space: nowrap; line-height: 1; }

  .title-caps { font-weight: 800; font-size: 20px; letter-spacing: 0.5px; text-transform: uppercase; color: var(--white); }
  .title { font-weight: 700; font-size: 22px; }
  .headline { font-weight: 700; font-size: 30px; color: var(--mauve-text); }
  .headline-light { font-weight: 400; font-size: 30px; color: var(--ink); }
  .promise { font-weight: 400; font-size: 15px; color: var(--ink); }
  .promise-accent { font-weight: 600; font-size: 14.5px; color: var(--mauve-text); }

  .pill { position: absolute; height: 22px; border-radius: 11px; display: flex; align-items: center; justify-content: center;
          font-weight: 700; font-size: 10.5px; color: var(--white); background: var(--mauve); white-space: nowrap; }
  .pill.join { font-size: 9px; letter-spacing: 0.6px; color: var(--ink); background: var(--cream-pill); }
  .pill.join.mauve { color: var(--white); background: var(--mauve); }

  .photo-pink { background: radial-gradient(ellipse at 50% 60%, #e7a9bb 0%, #f5c9d6 45%, #fde6ee 80%); }
  .photo-dark { background: radial-gradient(ellipse at 50% 70%, #3a2a2a 0%, #6a4a44 45%, #f5c9d6 85%); }
  .photo-brown { background: radial-gradient(ellipse at 50% 55%, #6d4a3c 0%, #8d5d45 55%, #9a6a50 100%); }
  .photo-fade { background: radial-gradient(ellipse at 50% 65%, #e7a9bb 0%, #f5c9d6 45%, rgba(253,230,238,0) 80%); }

  .side-word { position: absolute; top: 18px; writing-mode: vertical-rl; font-weight: 800; font-size: 19px;
               color: var(--side-word); text-transform: uppercase; white-space: nowrap; letter-spacing: 0.5px; line-height: 1; }
</style>
</head>
<body>

<!-- Tile 1 -->
<section class="tile col-a row-1" style="background: var(--pink);">
  <div class="box photo-pink" style="left:7px; top:7px; width:342px; height:198px; border-radius:8px 8px 0 0;" role="img" aria-label="Four smiling women in sports bras and leggings standing arm in arm"></div>
  <div class="line title-caps" style="top:230px;">45 Glow Challenge</div>
  <div class="box" style="left:7px; top:255px; width:342px; height:78px; background: var(--pink-light); border-radius:0 0 8px 8px;"></div>
  <div class="line headline" style="top:279px; font-size:28px;">Ninety Days Bold:</div>
  <div class="line promise" style="top:306px;">Lose Up to 20 Pounds in 6 Weeks!</div>
  <div class="pill" style="left:105px; top:322px; width:147px;">Begins Monday, Jan 6th</div>
</section>

<!-- Tile 2 -->
<section class="tile col-b row-1" style="background: var(--pink);">
  <div class="line title" style="top:29px; color: var(--ink);">45 Glow Challenge</div>
  <div class="box" style="left:7px; top:56px; width:342px; height:277px; background: linear-gradient(var(--pink-pale), var(--pink-light)); border-radius:0 0 8px 8px;"></div>
  <div class="line headline" style="top:80px;">Ninety Days Bold:</div>
  <div class="line promise" style="top:107px;">Lose Up to 20 Pounds in 6 Weeks!</div>
  <div class="pill" style="left:97px; top:123px; width:161px;">Begins Monday, Jan 6th</div>
  <div class="box photo-dark" style="left:20px; top:153px; width:316px; height:180px;" role="img" aria-label="Five women of different ages in black bodysuits posing together"></div>
  <div class="pill join mauve" style="left:131px; top:323px; width:94px;">JOIN US &gt;&gt;</div>
</section>

<!-- Tile 3 -->
<section class="tile col-a row-2" style="background: var(--mauve);">
  <div class="line title-caps" style="top:29px;">45 Glow Challenge</div>
  <div class="box" style="left:7px; top:56px; width:342px; height:79px; background: linear-gradient(var(--pink-light), var(--pink-pale));"></div>
  <div class="line headline" style="top:78px; font-size:28px;">Ninety Days Bold:</div>
  <div class="line promise" style="top:105px;">Lose Up to 20 Pounds in 6 Weeks!</div>
  <div class="box photo-brown" style="left:7px; top:135px; width:342px; height:198px; border-radius:0 0 8px 8px;" role="img" aria-label="Five women in sports bras hugging and smiling against a brown backdrop"></div>
  <div class="pill" style="left:105px; top:124px; width:147px;">Begins Monday, Jan 6th</div>
  <div class="pill join" style="left:131px; top:322px; width:94px;">JOIN US &gt;&gt;</div>
</section>

<!-- Tile 4 -->
<section class="tile col-b row-2" style="background: var(--cream);">
  <div class="box photo-pink" style="left:7px; top:7px; width:342px; height:194px; border-radius:8px 8px 0 0;" role="img" aria-label="Four smiling women in activewear standing arm in arm"></div>
  <div class="box" style="left:7px; top:201px; width:342px; height:39px; background: var(--mauve);"></div>
  <div class="line title" style="top:221px; color: var(--white);">45 Glow Challenge</div>
  <div class="box" style="left:7px; top:240px; width:342px; height:93px; background: var(--pink); border-radius:0 0 8px 8px;"></div>
  <div class="line headline" style="top:270px; font-size:31px;">Ninety Days Bold:</div>
  <div class="line promise" style="top:299px; font-size:16px;">Lose Up to <b>20 Pounds</b> in <b>6 Weeks!</b></div>
  <div class="pill" style="left:97px; top:321px; width:161px;">Begins Monday, Jan 6th</div>
</section>

<!-- Tile 5 -->
<section class="tile col-a row-3" style="background: var(--pink);">
  <svg class="box" style="left:0; top:0;" width="356" height="356" viewBox="0 0 356 356" aria-hidden="true">
    <defs>
      <linearGradient id="arch-fill" x1="0" y1="0" x2="0" y2="1">
        <stop offset="0" stop-color="#fde6ee"/><stop offset="1" stop-color="#fff6f8"/>
      </linearGradient>
    </defs>
    <path d="M40 7 H316 C340 60 336 120 326 170 C312 240 340 300 350 356 H6 C16 300 44 240 30 170 C20 120 16 60 40 7 Z" fill="url(#arch-fill)"/>
  </svg>
  <div class="line title" style="top:44px; color: var(--mauve-text);">45 Glow Challenge</div>
  <div class="pill" style="left:84px; top:61px; width:188px; height:23px; font-size:12px;">Begins Monday, Jan 6th</div>
  <div class="line headline-light" style="top:111px;">Ninety Days Bold:</div>
  <div class="line promise-accent" style="top:138px;">Lose Up to 20 Pounds in 6 Weeks!</div>
  <div class="pill join" style="left:139px; top:153px; width:77px;">JOIN US &gt;&gt;</div>
  <div class="box photo-fade" style="left:14px; top:180px; width:328px; height:176px;" role="img" aria-label="Four smiling women in sports bras and leggings standing arm in arm"></div>
</section>

<!-- Tile 6: text only -->
<section class="tile col-b row-3" style="background: var(--mauve);">
  <div class="box" style="left:7px; top:7px; width:342px; height:342px; background: linear-gradient(var(--pink-pale), #f8e6e2); border-radius:8px;"></div>
  <div class="side-word" style="left:14px;">45 Glow Challenge</div>
  <div class="side-word" style="right:14px;">45 Glow Challenge</div>
  <div class="pill" style="left:84px; top:96px; width:188px; height:24px; font-size:12px;">Begins Monday, Jan 6th</div>
  <div class="line title" style="top:146px; color: var(--mauve-text);">45 Glow Challenge</div>
  <div class="line headline-light" style="top:190px; font-size:31px;">Ninety Days Bold:</div>
  <div class="line promise-accent" style="top:226px;">Lose Up to 20 Pounds in 6 Weeks!</div>
</section>

</body>
</html>
```